Design music inspired artwork for Tunelark

Your job is to design/create artwork that captures how music makes people feel.

Tunelark is looking to engage their audience of 18-24 year-olds for whom music plays an important role in developing their identity, navigating life, and connecting with people around them.

Music is a short cut to our emotions. And, music has always been part of our social experience. Tunelark believes music helps people express how they’re #RightThisBeat, and that discovering and sharing music with friends makes our connection to each other richer.
Tunelark is creating a campaign that shares people's #RightThisBeat stories of connecting with each other through music, enabled by Tunelark. Our objective is to showcase playful - but honest - moments between people, and in doing so showcase how the platform enables discovery, sharing, and conversation through music.

Tunelark invites artists and designers to submit artwork that best captures how music makes people feel and brings them together.

Submissions must capture one or all of:
- The feeling of listening to music with friends, families, loved ones
- a first dance or first kiss
- friends or people connecting at a festival
- How music unites people from all cultures and backgrounds
- How music moves us
- A vision of what you hear and feel when listening to a song
- Communicating something when words are not enough

The goal of the winning submissions is to use them across Tunelark's channels, to inspire their audience to create and share music playlists and use the many features of the platform. They will also be showcased as part of an official Tunelark event.

Tunelark & Brushvault understand that artists will have their own interpretation of the brief so be sure to include a description with your submission and share the Tunelark song or playlist that inspired it so we can follow your creative process.
To be eligible for full prizing, please set up a Brushvault profile and upload your design via Brushvault:

https://www.brushvault-example.com/i/design-for-tunelark

The SketchHive project has 3 places, and the Brushvault package is even bigger! One overall winner will receive:
- $2,500
- Exposure across Tunelark social channels
- Their work showcased as part of an exclusive event in London
- A Tunelark Plus Account for 12 months
- The opportunity to feature in a Tunelark paid media campaign and/or to have future work commissioned by Tunelark
- A minimum of 20 finalists will have their work showcased as part of an event – to be viewed by key senior figures within the creative, media and music industries.

Guidelines:
- Artists should retain their original artwork files (in 300dpi) but designs must be submitted in JPEG or PNG, max size 5MB
- All entries must be original artwork (meaning not using third party pre-existing copyright materials) - photographs will not be accepted.
- Artists must join Brushvault using an active email address in order to ensure they can be contacted should they be selected.

Judging panel:
MARGOT PELLINGHAM (VP Creative and Brands Strategy at Tunelark)
TOBIAS RENQVIST (Director of Design, Communications at Tunelark)
GREG MALLORY (Executive Creative Director of independent, London ad agency Kettle and Kite)
OWEN PRATLEY (Co-founder at Paper Orbit)

*NB: Please do not include logos or the hashtag on your artwork- these can be added to the winning design once it has been selected.

Incentives have been increased!  We look forward to seeing your submissions.

If anyone has any questions or issues with the brief, please do not hesitate to ask.

Target Market(s)

Target market:

18-24 year-olds for whom music plays an important role in developing their identity, navigating life, and connecting with people around them.

Industry/Entity Type

Ad Agency

Requirements
Must have
• - Designers are required to submit their design to Brushvault as well as SketchHive (to be eligible for the Brushvault prize packages).
Nice to have
• - A full Brushvault profile to be reviewed by the judging panel (a very good way to get more of your work noticed by the panel of expert judges!)
Should not have
• - Profanities, illicit substances, anything offensive

```html
<!DOCTYPE html>
<html lang="en">
<head>
<meta charset="utf-8">
<title>Tunelark – Music is like rain</title>
<link rel="stylesheet" href="https://fonts.googleapis.com/css2?family=Pinyon+Script&display=swap">
<style>
  :root {
    --backdrop: #e6e7e8;
    --card-border: #ffffff;
    --card-fill: #000000;
    --rain-blue: #1f5f9e;
    --rain-deep: #0b2f5c;
    --rain-light: #3f86c4;
    --flame: #e8561c;
    --flame-glow: #f7b52a;
    --wave-blue: #3a7fb8;
    --quote: #ffffff;
    --brand-text: #111111;
  }
  * { margin: 0; padding: 0; box-sizing: border-box; }
  html, body {
    width: 1200px;
    height: 743px;
    overflow: hidden;
    background: var(--backdrop);
  }
  .canvas {
    position: relative;
    width: 1200px;
    height: 743px;
    background: var(--backdrop);
  }
  .card {
    position: absolute;
    left: 42px;
    top: 66px;
    width: 1116px;
    height: 614px;
    border: 4px solid var(--card-border);
    border-radius: 42px;
    background: var(--card-fill);
    overflow: hidden;
    box-shadow: 0 3px 10px rgba(0, 0, 0, 0.25);
  }
  .rain-art {
    position: absolute;
    left: 0;
    top: 0;
    width: 100%;
    height: 380px;
    background:
      linear-gradient(180deg,
        var(--rain-light) 0%,
        var(--rain-blue) 35%,
        var(--rain-deep) 70%,
        rgba(0, 0, 0, 0) 100%);
  }
  .guitar-art {
    position: absolute;
    left: 400px;
    top: 300px;
    width: 310px;
    height: 310px;
    background:
      radial-gradient(ellipse 30% 45% at 52% 62%, var(--flame-glow) 0%, var(--flame) 45%, rgba(232, 86, 28, 0) 100%),
      radial-gradient(ellipse 30% 40% at 75% 65%, var(--wave-blue) 0%, rgba(58, 127, 184, 0) 100%),
      radial-gradient(ellipse 28% 40% at 28% 65%, var(--flame) 0%, rgba(232, 86, 28, 0) 100%);
  }
  .quote {
    position: absolute;
    font-family: "Pinyon Script", cursive;
    font-weight: 400;
    color: var(--quote);
    font-size: 82px;
    line-height: 1;
    white-space: nowrap;
  }
  .quote-first { left: 116px; top: 292px; }
  .quote-second { left: 408px; top: 370px; }
  .brand-name {
    position: absolute;
    left: 1010px;
    top: 684px;
    width: 150px;
    text-align: center;
    font-family: "Pinyon Script", cursive;
    font-weight: 400;
    font-size: 36px;
    line-height: 1.3;
    color: var(--brand-text);
    white-space: nowrap;
  }
</style>
</head>
<body>
  <main class="canvas">
    <section class="card">
      <div class="rain-art" role="img" aria-label="Blue grunge paint drips falling from the top, filled with white music notes and treble clefs"></div>
      <div class="guitar-art" role="img" aria-label="Electric guitar with a speaker, framed by orange flame and blue wave swirls"></div>
      <p class="quote quote-first">Music is like rain.</p>
      <p class="quote quote-second">It falls everywhere!!</p>
    </section>
    <p class="brand-name">Tunelark</p>
  </main>
</body>
</html>
```